KMR Business cards

I currently have a logo that was designed by a pixel harbor designer. I would like this to be added to the business card.

We are an innovative new start-up business offering finance solutions to the car dealership market in the UK. So our clients are quiet traditional, so are cards need to fit in, but at the same time show we are a modern online business.

Finance

```html
<!DOCTYPE html>
<html lang="en">
<head>
<meta charset="utf-8">
<title>KMR Business Cards</title>
<link href="https://fonts.googleapis.com/css2?family=Arimo:wght@700&family=Mulish:wght@400;800&display=swap" rel="stylesheet">
<style>
  :root {
    --navy: #142a4e;
    --slate: #a4b5ba;
    --paper: #ffffff;
    --backdrop: #ffffff;
  }
  * { margin: 0; padding: 0; box-sizing: border-box; }
  html, body { width: 1200px; height: 1000px; overflow: hidden; background: var(--backdrop); }
  .canvas { position: relative; width: 1200px; height: 1000px; }

  .card {
    position: absolute;
    width: 522px;
    height: 299px;
    background: var(--paper);
    overflow: hidden;
    border: 1px solid #eef0f1;
  }
  .card-front { left: 351px; top: 188px; }
  .card-back { left: 349px; top: 536px; width: 524px; }
  .card-shape { position: absolute; inset: 0; width: 100%; height: 100%; }

  .brand-name {
    position: absolute;
    display: flex;
    align-items: center;
    gap: 8px;
    white-space: nowrap;
  }
  .brand-dot {
    display: block;
    width: 16px;
    height: 16px;
    border-radius: 50%;
  }
  .card-front .brand-name {
    left: 128px; top: 136px; height: 48px;
    color: var(--navy);
    font-family: "Mulish", "Century Gothic", sans-serif;
    font-weight: 800;
    font-size: 40px;
  }
  .card-front .brand-dot { background: var(--navy); }
  .card-back .brand-name {
    left: 40px; top: 82px; height: 50px;
    color: var(--paper);
    font-family: "Arimo", Arial, sans-serif;
    font-weight: 700;
    font-size: 44px;
  }
  .card-back .brand-dot { background: var(--paper); }

  .company-name {
    position: absolute;
    left: 266px; top: 96px;
    color: var(--navy);
    font-family: "Mulish", "Century Gothic", sans-serif;
    line-height: 44px;
  }
  .company-name span { display: block; font-size: 39px; font-weight: 400; }
  .company-name .company-name-strong { font-weight: 800; font-size: 37px; }

  .tagline {
    position: absolute;
    left: 0; width: 212px; top: 228px;
    text-align: center;
    color: var(--paper);
    font-family: "Arimo", Arial, sans-serif;
    font-weight: 700;
    font-size: 20px;
    line-height: 25px;
  }

  .contact {
    position: absolute;
    right: 12px;
    text-align: right;
    color: var(--navy);
    font-family: "Arimo", Arial, sans-serif;
    font-weight: 700;
    font-size: 14.5px;
    line-height: 17.5px;
    letter-spacing: 0.2px;
    white-space: nowrap;
  }
  .contact-person { top: 129px; }
  .contact-lines { top: 182px; }
  .contact-email { top: 271px; }
</style>
</head>
<body>
<main class="canvas">

  <section class="card card-front" aria-label="Business card front">
    <svg class="card-shape" viewBox="0 0 522 299" preserveAspectRatio="none" aria-hidden="true">
      <polygon points="339,0 522,0 522,299 195,299" fill="var(--slate)"/>
    </svg>
    <div class="brand-name"><span class="brand-dot"></span>KMR</div>
    <h1 class="company-name">
      <span>Key</span>
      <span>Motor</span>
      <span class="company-name-strong">Repay</span>
    </h1>
  </section>

  <section class="card card-back" aria-label="Business card back">
    <svg class="card-shape" viewBox="0 0 524 299" preserveAspectRatio="none" aria-hidden="true">
      <polygon points="0,0 328,0 182,299 0,299" fill="var(--navy)"/>
    </svg>
    <div class="brand-name"><span class="brand-dot"></span>KMR</div>
    <p class="tagline">DRIVE NOW,<br>PAY LATER</p>

    <div class="contact contact-person">
      <p class="person-name">DANIEL HARLOW</p>
      <p class="person-role">Founder</p>
    </div>
    <div class="contact contact-lines">
      <p class="contact-phone">07700 900418</p>
      <p class="contact-handle">daniel.harlow_kmr</p>
      <p class="contact-web">www.keymotorrepay.com</p>
    </div>
    <p class="contact contact-email">daniel.harlow@keymotorrepay.com</p>
  </section>

</main>
</body>
</html>
```